Defense contractor needs a roll-up for an exhibition

The booth we have booked has only a size of 3m².
So this will be the centerpiece of the whole booth.
We need a roll-up that attracts visitors and at the same time it should contain already designed graphics. These graphics are giving visitors an overview of our system. So it is necessary to have them exposed in a height that the booth personal can conveniently point with its fingers at them.
For information about our company and product visit:
https://www.corvantilmetrics.com/
For designing you should use Adobe Illustrator and the templates provided in the zip file, to guarantee a perfect print.
I have supplied my business card that you can copy the logo. As the company logo will be already at the booth nearby the top of the roll-up, you should not place it there. It can be in the middle or at the bottom.
I have uploaded a picture of the booth. The roll up will be placed at the left of the screen and has a size of 80cm x 200cm

Defense

Defense

Serif

0054AA
0677BA
7BADD7
CADEEF
E8F1F8

Must have
• you must use the Adobe Illustrator template to have a good printing result
Should not have
• company logo on the upper side of the roll-up

```html
<!DOCTYPE html>
<html lang="en">
<head>
<meta charset="utf-8">
<title>Corvantil Metrics – Roll-up</title>
<link href="https://fonts.googleapis.com/css2?family=Anton&family=Poppins:wght@400;500;600;700;800&family=Roboto+Condensed:wght@700&display=swap" rel="stylesheet">
<style>
  :root{
    --stage:#eeeeee;
    --brand-blue:#1f2f96;
    --brand-navy:#101a66;
    --ink:#0d0d0d;
    --panel:#141414;
    --paper:#ffffff;
    --icon-blue:#2338a6;
    --lavender:#e8e9f6;
    --sky-pink:#e0a2b8;
    --sky-peach:#f0c2a8;
    --sky-mid:#5a6ac4;
    --scene-grey:#9a9cb0;
    --scene-dark:#5c5f74;
  }
  *{margin:0;padding:0;box-sizing:border-box}
  html,body{width:1200px;height:4000px;overflow:hidden;background:var(--stage)}
  .rollup{position:absolute;left:40px;top:620px;width:1120px;height:2761px;background:var(--paper);overflow:hidden;font-family:"Poppins",sans-serif}
  .layer{position:absolute;left:0;width:1120px}
  .header{top:0;height:151px;background:var(--brand-blue)}
  .header svg{position:absolute;inset:0}
  .brand-name{position:absolute;top:0;left:0;width:1120px;height:151px;display:flex;align-items:center;justify-content:center;font-family:"Anton",sans-serif;font-size:56px;color:var(--ink);letter-spacing:1px}
  .hero{top:151px;height:800px;background:linear-gradient(180deg,var(--brand-navy) 0%,var(--brand-blue) 40%,#2b3aa8 52%,#3a47a8 100%)}
  .hero-title{position:absolute;top:40px;left:0;width:1120px;text-align:center;font-family:"Anton",sans-serif;color:var(--paper);font-size:128px;line-height:128px;letter-spacing:1px;z-index:1}
  .hero-sub{position:absolute;top:312px;left:0;width:1120px;text-align:center;font-weight:800;font-size:52px;color:var(--paper);z-index:1}
  .hero-scene{position:absolute;top:370px;left:0;width:1120px;height:430px;
    background:
      radial-gradient(ellipse 300px 90px at 300px 170px,rgba(240,194,168,.85),rgba(224,162,184,.55) 45%,transparent 75%),
      radial-gradient(ellipse 380px 110px at 180px 220px,rgba(224,162,184,.7),transparent 70%),
      radial-gradient(ellipse 320px 120px at 900px 170px,rgba(200,150,190,.55),transparent 70%),
      radial-gradient(ellipse 420px 80px at 620px 250px,rgba(120,130,210,.6),transparent 70%),
      linear-gradient(180deg,transparent 0%,transparent 55%,rgba(13,13,13,.85) 72%,var(--ink) 86%,var(--ink) 100%);}
  .services-band{top:943px;height:148px;background:var(--ink)}
  .services-band svg{position:absolute;inset:0}
  .services-title{position:absolute;top:60px;left:0;width:1120px;height:88px;display:flex;align-items:center;justify-content:center;font-weight:800;font-size:104px;color:var(--ink);line-height:1}
  .panel{position:absolute;left:60px;top:1136px;width:998px;height:787px;background:var(--panel);border-radius:44px}
  .panel-intro{position:absolute;top:28px;left:0;width:998px;text-align:center;color:var(--paper);font-size:33px;line-height:42px;font-weight:400}
  .divider{position:absolute;left:529px;top:161px;width:3px;height:588px;background:#555}
  .service{position:absolute;width:480px;text-align:center;color:var(--paper)}
  .service svg{display:block;margin:0 auto;width:184px;height:184px}
  .service-label{font-weight:500;font-size:41px;line-height:58px;margin-top:10px}
  .tagline-band{top:1974px;height:149px;background:var(--brand-blue)}
  .tagline-band svg{position:absolute;inset:0}
  .tagline{position:absolute;top:0;left:0;width:1120px;height:149px;display:flex;align-items:center;justify-content:center;text-align:center;font-weight:600;font-size:38px;line-height:50px;color:var(--ink)}
  .system-overview{top:2123px;height:461px;
    background:
      radial-gradient(ellipse 150px 110px at 170px 190px,rgba(154,156,176,.75),transparent 75%),
      radial-gradient(ellipse 90px 60px at 420px 90px,rgba(154,156,176,.55),transparent 75%),
      radial-gradient(ellipse 200px 150px at 560px 330px,rgba(92,95,116,.55),rgba(154,156,176,.4) 50%,transparent 78%),
      radial-gradient(ellipse 240px 160px at 940px 170px,rgba(154,156,176,.7),transparent 75%),
      radial-gradient(ellipse 200px 110px at 930px 290px,rgba(92,95,116,.45),transparent 75%),
      linear-gradient(180deg,var(--lavender),#dcdff2);}
  .footer{top:2584px;height:177px;background:var(--brand-blue)}
  .footer svg{position:absolute;inset:0}
  .web{position:absolute;top:0;left:0;width:1120px;height:177px;display:flex;align-items:center;justify-content:center;font-family:"Roboto Condensed",sans-serif;font-weight:700;font-size:64px;color:var(--paper);letter-spacing:2px}
</style>
</head>
<body>
<main class="rollup">
  <header class="layer header">
    <svg width="1120" height="151" viewBox="0 0 1120 151"><polygon points="55,0 1065,0 1005,151 115,151" fill="var(--paper)"/></svg>
    <div class="brand-name">CORVANTIL METRICS</div>
  </header>

  <section class="layer hero">
    <h1 class="hero-title">ADVANCED COMBAT<br>TRAINING SYSTEMS</h1>
    <p class="hero-sub">FOR REALISTIC COMBAT SIMULATION</p>
    <div class="hero-scene" role="img" aria-label="Tank silhouette on a grassy ridge against a dusk sky"></div>
  </section>

  <section class="layer services-band">
    <svg width="1120" height="148" viewBox="0 0 1120 148"><polygon points="255,60 856,60 876,148 215,148" fill="var(--paper)"/></svg>
    <h2 class="services-title">SERVICES</h2>
  </section>

  <section class="panel">
    <p class="panel-intro">The signature of the contract is not the end - it is just the<br>beginning of a long-lasting partnership.We offer</p>
    <div class="divider"></div>

    <div class="service" style="left:24px;top:138px">
      <svg viewBox="0 0 184 184"><circle cx="92" cy="92" r="88" fill="var(--paper)"/><circle cx="92" cy="92" r="80" fill="var(--icon-blue)"/>
        <g fill="none" stroke="var(--paper)" stroke-width="4"><circle cx="92" cy="92" r="44" stroke-dasharray="10 6"/><circle cx="92" cy="92" r="30"/><polyline points="78,92 89,103 107,82"/></g></svg>
      <p class="service-label">Extended<br>Warranty Programs</p>
    </div>
    <div class="service" style="left:541px;top:138px">
      <svg viewBox="0 0 184 184"><circle cx="92" cy="92" r="88" fill="var(--paper)"/><circle cx="92" cy="92" r="80" fill="var(--icon-blue)"/>
        <g fill="none" stroke="var(--paper)" stroke-width="4"><path d="M120 72 A40 40 0 1 0 90 132"/><polyline points="92,68 92,96 104,104"/><path d="M104 118 c6-10 16-10 16 0 s10 10 16 0 c-6-10-16-10-16 0 s-10 10-16 0z"/></g></svg>
      <p class="service-label">Long-term Spare<br>Part Services</p>
    </div>
    <div class="service" style="left:24px;top:457px">
      <svg viewBox="0 0 184 184"><circle cx="92" cy="92" r="88" fill="var(--paper)"/><circle cx="92" cy="92" r="80" fill="var(--icon-blue)"/>
        <g fill="none" stroke="var(--paper)" stroke-width="4"><rect x="60" y="54" width="62" height="82" rx="5"/><rect x="78" y="46" width="26" height="14" rx="3"/><line x1="70" y1="78" x2="110" y2="78"/><line x1="70" y1="92" x2="104" y2="92"/><line x1="70" y1="106" x2="96" y2="106"/><line x1="104" y1="126" x2="130" y2="90"/></g></svg>
      <p class="service-label">Maintenance<br>Contracts</p>
    </div>
    <div class="service" style="left:541px;top:457px">
      <svg viewBox="0 0 184 184"><circle cx="92" cy="92" r="88" fill="var(--paper)"/><circle cx="92" cy="92" r="80" fill="var(--icon-blue)"/>
        <g fill="none" stroke="var(--paper)" stroke-width="4"><path d="M56 96 V86 a36 36 0 0 1 72 0 V96"/><rect x="48" y="88" width="14" height="26" rx="5"/><rect x="122" y="88" width="14" height="26" rx="5"/><path d="M129 114 q0 18 -24 18 h-8"/><path d="M58 140 q34 -18 68 0"/></g></svg>
      <p class="service-label" style="margin-top:40px">Logistics Support</p>
    </div>
  </section>

  <section class="layer tagline-band">
    <svg width="1120" height="149" viewBox="0 0 1120 149">
      <polygon points="188,0 943,0 987,149 144,149" fill="var(--paper)"/>
      <polygon points="158,0 178,0 134,149 114,149" fill="var(--paper)"/>
      <polygon points="953,0 973,0 1017,149 997,149" fill="var(--paper)"/>
    </svg>
    <p class="tagline">EQUIP YOUR FIGHTING<br>FORCE WITH PRECISION TRAINING</p>
  </section>

  <section class="layer system-overview" role="img" aria-label="Isometric overview of the training system: tanks, target stations, mobile command vehicle and instructor room"></section>

  <footer class="layer footer">
    <svg width="1120" height="177" viewBox="0 0 1120 177"><polygon points="0,0 1120,0 1120,10 1050,177 70,177 0,10" fill="var(--ink)"/></svg>
    <p class="web">www.corvantilmetrics.com</p>
  </footer>
</main>
</body>
</html>
```